Lodging Refresh Partners - Tabletop Display

We need a 5'x5' trade show display for a hotel renovation company named "Lodging Refresh Partners." Lodging Refresh Partners is the most complete authority on hotel renovation in the country, and we're the only 100% turn-key renovator in Colorado. With one phone call, we deliver an approved design, FF&E purchasing, logistics, construction, installation, and warranty administration. The design needs to convey professionalism. Our goal is to help our clients reduce costs and reduce stress while achieving the best results. The colors should align with the attached brochure for our Raleigh office.

Target Market(s)

Hotel owners and general managers

Industry/Entity Type

Design Agency

Colors
3277b5
85acd3
cfdeed

Requirements
Must have
• Our product is a blend of design and construction. I need to convey our services and attention to detail without seeming salesy, bold, or aggressive. The goal is to convey confidence and help to relax our potential client base.
Nice to have
• Possibly one or more photos of completed projects. Not sure if exterior, lobby, or guest room photos would be best. I can send files via dropbox if that's helpful.
Should not have
• I've included a photo of the old display at a trade show. I strongly dislike the yellow and red on the display. Please try to stick to the color palette of the attached brochure.

```html
<!DOCTYPE html>
<html lang="en">
<head>
<meta charset="utf-8">
<title>Lodging Refresh Partners – Tabletop Display</title>
<link rel="stylesheet" href="https://fonts.googleapis.com/css2?family=Questrial&family=Yanone+Kaffeesatz:wght@400&display=swap">
<style>
  :root {
    --navy: #252c37;
    --blue: #2b64a1;
    --white: #ffffff;
    --ink: #1f2733;
    --lobby-tone: #b99873;
    --room-tone: #3a3d42;
    --guest-tone: #d9d7d3;
  }
  * { margin: 0; padding: 0; box-sizing: border-box; }
  html, body { width: 960px; height: 1200px; overflow: hidden; background: var(--white); }
  .display {
    position: absolute; left: 32px; top: 152px; width: 898px; height: 898px;
    background: var(--white);
    box-shadow: 8px 10px 6px rgba(0,0,0,0.6);
    font-family: "Questrial", sans-serif;
  }
  .display > * { position: absolute; }
  .headline-bar {
    left: 0; top: 0; width: 898px; height: 100px; background: var(--navy);
    color: var(--white); display: flex; align-items: center; justify-content: center;
    font-size: 42px; letter-spacing: 0.5px; text-transform: uppercase;
  }
  .photo-lobby { left: 0; top: 112px; width: 481px; height: 384px; background: var(--lobby-tone); }
  .brand {
    left: 494px; top: 112px; width: 404px; height: 174px;
    display: flex; align-items: center; justify-content: center; gap: 14px;
  }
  .brand-mark { width: 26px; height: 26px; background: var(--blue); flex: none; }
  .brand-name { font-size: 30px; color: var(--blue); line-height: 1.15; }
  .photo-room { left: 494px; top: 290px; width: 404px; height: 206px; background: var(--room-tone); }
  .benefits {
    left: 494px; top: 290px; width: 404px; height: 206px;
    list-style: none; padding: 30px 0 0 100px;
    font-family: "Yanone Kaffeesatz", sans-serif; font-size: 46px; line-height: 47px;
    color: var(--white); text-transform: uppercase;
  }
  .benefits li::before {
    content: ""; display: inline-block; width: 15px; height: 15px; border-radius: 50%;
    background: var(--white); margin-right: 5px; vertical-align: 6px;
  }
  .services {
    left: 0; top: 508px; width: 509px; height: 198px; background: var(--blue);
    color: var(--white); font-family: "Yanone Kaffeesatz", sans-serif; font-size: 34px;
  }
  .service-col { position: absolute; top: 23px; list-style: none; }
  .service-col.first { left: 34px; }
  .service-col.second { left: 208px; }
  .service-col li { height: 38px; display: flex; align-items: center; gap: 12px; white-space: nowrap; }
  .tick { width: 15px; height: 15px; flex: none; }
  .photo-guest { left: 522px; top: 508px; width: 376px; height: 198px; background: var(--guest-tone); }
  .closing-bar {
    left: 0; top: 718px; width: 898px; height: 112px; background: var(--navy);
    color: var(--white); text-align: center; padding-top: 8px;
  }
  .closing-lead { font-size: 32px; line-height: 38px; letter-spacing: 0.5px; }
  .closing-call { font-size: 56px; line-height: 60px; text-transform: uppercase; }
  .web-address {
    left: 0; top: 830px; width: 898px; height: 68px;
    display: flex; align-items: center; justify-content: center;
    font-size: 40px; letter-spacing: 4px; color: var(--ink);
  }
  .web-address .accent { color: var(--blue); }
</style>
</head>
<body>
<main class="display">
  <header class="headline-bar">We will do your entire renovation</header>

  <div class="photo-lobby" role="img" aria-label="Photo of a renovated hotel lobby with a stone fireplace, sofa and chandelier"></div>

  <div class="brand">
    <span class="brand-mark"></span>
    <span class="brand-name">Lodging Refresh Partners</span>
  </div>

  <div class="photo-room" role="img" aria-label="Photo of a dimly lit renovated guest room with a bed and television"></div>
  <ul class="benefits">
    <li>Lowest cost</li>
    <li>Least hassle</li>
    <li>Best results</li>
  </ul>

  <section class="services">
    <ul class="service-col first">
      <li><svg class="tick" viewBox="0 0 15 15"><rect x="0.75" y="0.75" width="13.5" height="13.5" fill="none" stroke="#fff" stroke-width="1.5"/><path d="M3.5 7.5 L6.5 10.5 L11.5 4" fill="none" stroke="#fff" stroke-width="1.6"/></svg>Planning</li>
      <li><svg class="tick" viewBox="0 0 15 15"><rect x="0.75" y="0.75" width="13.5" height="13.5" fill="none" stroke="#fff" stroke-width="1.5"/><path d="M3.5 7.5 L6.5 10.5 L11.5 4" fill="none" stroke="#fff" stroke-width="1.6"/></svg>Design</li>
      <li><svg class="tick" viewBox="0 0 15 15"><rect x="0.75" y="0.75" width="13.5" height="13.5" fill="none" stroke="#fff" stroke-width="1.5"/><path d="M3.5 7.5 L6.5 10.5 L11.5 4" fill="none" stroke="#fff" stroke-width="1.6"/></svg>Specification</li>
      <li><svg class="tick" viewBox="0 0 15 15"><rect x="0.75" y="0.75" width="13.5" height="13.5" fill="none" stroke="#fff" stroke-width="1.5"/><path d="M3.5 7.5 L6.5 10.5 L11.5 4" fill="none" stroke="#fff" stroke-width="1.6"/></svg>FF&amp;E</li>
    </ul>
    <ul class="service-col second">
      <li><svg class="tick" viewBox="0 0 15 15"><rect x="0.75" y="0.75" width="13.5" height="13.5" fill="none" stroke="#fff" stroke-width="1.5"/><path d="M3.5 7.5 L6.5 10.5 L11.5 4" fill="none" stroke="#fff" stroke-width="1.6"/></svg>Logistics</li>
      <li><svg class="tick" viewBox="0 0 15 15"><rect x="0.75" y="0.75" width="13.5" height="13.5" fill="none" stroke="#fff" stroke-width="1.5"/><path d="M3.5 7.5 L6.5 10.5 L11.5 4" fill="none" stroke="#fff" stroke-width="1.6"/></svg>Construction</li>
      <li><svg class="tick" viewBox="0 0 15 15"><rect x="0.75" y="0.75" width="13.5" height="13.5" fill="none" stroke="#fff" stroke-width="1.5"/><path d="M3.5 7.5 L6.5 10.5 L11.5 4" fill="none" stroke="#fff" stroke-width="1.6"/></svg>Installation</li>
      <li><svg class="tick" viewBox="0 0 15 15"><rect x="0.75" y="0.75" width="13.5" height="13.5" fill="none" stroke="#fff" stroke-width="1.5"/><path d="M3.5 7.5 L6.5 10.5 L11.5 4" fill="none" stroke="#fff" stroke-width="1.6"/></svg>Warranty Administration</li>
    </ul>
  </section>

  <div class="photo-guest" role="img" aria-label="Photo of a bright renovated guest room with two beds, desk and television"></div>

  <section class="closing-bar">
    <p class="closing-lead">A Complete Renovation with</p>
    <p class="closing-call">Just one call!</p>
  </section>

  <footer class="web-address">www.<span class="accent">lodging</span>refresh.com</footer>
</main>
</body>
</html>
```